Corporate consulting business needs a business card

I want a professional business card.... surprise me

Updates

Reason: i dont think 2 days is enough

Target Market(s)

Corprorate and Not for Profit firms and organisations

Industry/Entity Type

Consulting

Contact Information for Business Card

Logo
Corporate Consulting Services
On Time, On Budget, Beyond Expectation
Tovan Presfield
Director
0427 31 94 62 (Larger)
tovan@tp-advisory.com.au
www.tp-advisory.com.au
include little icons beside the contact info:

- Envelope = email
- Phone = phone
- Globe = website

Font styles to use
Serif
Sans Serif

Requirements
Must have
• Professional and clean
Nice to have
• you tell me

```html
<!DOCTYPE html>
<html lang="en">
<head>
<meta charset="utf-8">
<title>TP Advisory Services – Business Card</title>
<link href="https://fonts.googleapis.com/css2?family=Lato:wght@300;400;700&display=swap" rel="stylesheet">
<style>
  :root{
    --bg:#3f4042;
    --stone:#dcd8d0;
    --stone-soft:#d8d4cc;
    --paper:#ffffff;
    --brown:#4e2a17;
    --brown-text:#5a3320;
    --ink:#2b1a12;
    --light:#f5efe9;
  }
  *{margin:0;padding:0;box-sizing:border-box}
  html,body{width:1200px;height:810px;overflow:hidden}
  body{background:var(--bg);font-family:"Lato",sans-serif;position:relative}
  .card{position:absolute;width:600px;height:343px;border-radius:22px;overflow:hidden;box-shadow:0 10px 24px rgba(0,0,0,.35)}
  .card--back{left:300px;top:28px;background:var(--stone)}
  .card--front{left:300px;top:415px;background:var(--paper)}

  .brand{display:flex;align-items:center;gap:12px;color:var(--brown-text);font-weight:700;font-size:26px;letter-spacing:1.5px;text-transform:uppercase;white-space:nowrap}
  .brand__dot{width:22px;height:22px;border:3px solid var(--brown-text);border-radius:50%;flex:none}
  .card--back .brand{position:absolute;left:0;right:0;top:120px;justify-content:center}
  .tagline{position:absolute;left:0;right:0;top:250px;text-align:center;color:var(--brown-text);font-size:17px;font-weight:700}
  .tagline span{margin:0 4px}

  .front-shape{position:absolute;inset:0}
  .card--front .brand{position:absolute;left:28px;top:156px;font-size:19px;gap:9px}
  .card--front .brand__dot{width:18px;height:18px;border-width:2.5px}

  .person{position:absolute;right:40px;top:52px;text-align:center;color:var(--light)}
  .person__name{font-weight:700;font-size:24px;letter-spacing:.5px;text-transform:uppercase;white-space:nowrap}
  .person__role{font-weight:300;font-size:14px;margin-top:2px}

  .contact{position:absolute;right:22px;top:175px;width:180px;text-align:center;color:var(--light);white-space:nowrap}
  .contact__icons{display:flex;justify-content:center;gap:8px;margin-bottom:10px}
  .contact__icons svg{width:24px;height:24px}
  .contact__phone{font-size:24px;font-weight:400;letter-spacing:.5px;margin-bottom:6px}
  .contact__line{font-size:13px;line-height:1.55}
</style>
</head>
<body>
  <section class="card card--back">
    <div class="brand"><span class="brand__dot"></span>TP Advisory Services</div>
    <p class="tagline"><span>• On Time</span><span>• On Budget</span><span>• Beyond Expectation</span></p>
  </section>

  <section class="card card--front">
    <svg class="front-shape" viewBox="0 0 600 343" preserveAspectRatio="none" aria-hidden="true">
      <path d="M238 0 Q392 150 336 343 L362 343 Q420 150 270 0 Z" fill="var(--stone-soft)"/>
      <path d="M278 0 Q430 150 372 343 L600 343 L600 0 Z" fill="var(--brown)"/>
    </svg>
    <div class="brand"><span class="brand__dot"></span>TP Advisory Services</div>

    <div class="person">
      <div class="person__name">Tovan Presfield</div>
      <div class="person__role">Director</div>
    </div>

    <div class="contact">
      <div class="contact__icons">
        <svg viewBox="0 0 24 24" aria-label="phone"><circle cx="12" cy="12" r="11" fill="var(--light)"/><path d="M9 6.5l2 2.5-1.2 1.4a8 8 0 0 0 3.8 3.8l1.4-1.2 2.5 2-1.2 2.2C11 17 7 13 6.8 7.7z" fill="var(--brown)"/></svg>
        <svg viewBox="0 0 24 24" aria-label="email"><circle cx="12" cy="12" r="11" fill="var(--light)"/><rect x="6" y="8" width="12" height="8" fill="var(--brown)"/><path d="M6 8l6 4.5L18 8" fill="none" stroke="var(--light)" stroke-width="1.2"/></svg>
        <svg viewBox="0 0 24 24" aria-label="website"><circle cx="12" cy="12" r="11" fill="var(--light)"/><g fill="none" stroke="var(--brown)" stroke-width="1.3"><circle cx="12" cy="12" r="6"/><ellipse cx="12" cy="12" rx="2.6" ry="6"/><path d="M6 12h12"/></g></svg>
      </div>
      <div class="contact__phone">0427 31 94 62</div>
      <div class="contact__line">tovan@tp-advisory.com.au</div>
      <div class="contact__line">www.tp-advisory.com.au</div>
    </div>
  </section>
</body>
</html>
```